Used Car Business Card Design

Maple Ridge Auto Sales is a woman owned women friendly car lot.  We focus on providing Professionalism, Integrity and Respect beginning with the initial introduction.  We place the highest importance on customer service after the sale and our rating with the TVB of Arkansas shows it.  We're starting out 7th year, recently relocated. Satisfied Clients bring their family members, friends and co-workers to buy their cars, SUV's and trucks from MRAS.
You buy here / you pay here, Lending program opportunities too, Great Cash Prices
Finance with Flexibility we look at each individual uniquely and not a credit score
I think of my kids when getting our vehicles ready and your safety when you drive away in a MRAS car. . .  Drive away with Peace of Mind...
Maroon, Black and Silver colors.

Updates
I sent a response to the designers - have  not heard from them, will I receive my funds back?

Thank you all,  a lot of great designs - Making my decision on Nov 4th

So much talent. . .
So very challenging. . .
Thank you for your participation.
Sincerely,
Maple Ridge Auto Sales
Lorna Pickett

Industry/Entity Type
Safety
Contact Information for Business Card
Maple Ridge Auto Sales
"A Sound Ride at a Fair Price"
4153 Garvey Rd. Harlow Springs, Ar 72990
Lorna Pickett
501.389.7312

```html
<!DOCTYPE html>
<html lang="en">
<head>
<meta charset="utf-8">
<title>Maple Ridge Auto Sales – Business Card</title>
<link rel="stylesheet" href="https://fonts.googleapis.com/css2?family=Mulish:wght@400;600;700&display=swap">
<style>
  :root {
    --backdrop: #efefef;
    --card: #ffffff;
    --band-silver: #dcdcdc;
    --ink: #3a3a3a;
    --ink-soft: #4a4a4a;
    --photo-dark: #2e3035;
    --photo-mid: #4a5058;
    --photo-light: #6a7078;
    --on-dark: #ffffff;
  }
  * { box-sizing: border-box; margin: 0; padding: 0; }
  html, body {
    width: 1200px; height: 720px; overflow: hidden;
    background: var(--backdrop);
    font-family: "Mulish", "Century Gothic", sans-serif;
  }
  .sheet {
    width: 1200px; height: 720px;
    display: flex; align-items: center; justify-content: center; gap: 50px;
  }
  .card {
    position: relative;
    width: 525px; height: 300px;
    background: var(--card);
    box-shadow: 0 2px 8px rgba(0,0,0,0.12);
    overflow: hidden;
  }
  /* Back of card */
  .card-back .silver-band {
    position: absolute; left: 0; right: 0; top: 45px; height: 195px;
    background: var(--band-silver);
    display: flex; flex-direction: column; align-items: center; justify-content: center;
    gap: 4px;
  }
  .card-back .company {
    font-weight: 700; font-size: 30px; color: var(--ink); letter-spacing: 0.2px;
  }
  .card-back .tagline {
    font-weight: 400; font-size: 20px; color: var(--ink-soft);
  }
  /* Front of card */
  .card-front .company {
    position: absolute; left: 40px; top: 26px;
    font-weight: 700; font-size: 26px; color: var(--ink);
  }
  .card-front .photo-band {
    position: absolute; left: 20px; right: 0; top: 68px; height: 150px;
    background: linear-gradient(100deg, var(--photo-light) 0%, var(--photo-mid) 25%, var(--photo-dark) 60%, var(--photo-dark) 100%);
  }
  .card-front .person {
    position: absolute; right: 40px; top: 122px;
    color: var(--on-dark); display: flex; align-items: baseline; gap: 10px;
  }
  .card-front .person-name {
    font-weight: 700; font-size: 17px; letter-spacing: 0.8px; text-transform: uppercase;
  }
  .card-front .person-role { font-weight: 600; font-size: 12px; }
  .card-front .contact {
    position: absolute; left: 40px; top: 228px;
    font-size: 14px; font-style: normal; color: var(--ink); line-height: 1.3;
  }
</style>
</head>
<body>
<main class="sheet">
  <section class="card card-back" aria-label="Card back">
    <div class="silver-band">
      <h1 class="company">Maple Ridge Auto Sales</h1>
      <p class="tagline">A Sound Ride at a Fair Price</p>
    </div>
  </section>

  <section class="card card-front" aria-label="Card front">
    <h2 class="company">Maple Ridge Auto Sales</h2>
    <div class="photo-band" role="img" aria-label="Dark photo of a row of cars on a lot, headlights in close-up"></div>
    <div class="person">
      <span class="person-name">Lorna Pickett</span>
      <span class="person-role">Manager</span>
    </div>
    <address class="contact">
      <div class="phone">501.389.7312</div>
      <div class="street">4153 Garvey Rd. Harlow Springs, Ar 72990</div>
    </address>
  </section>
</main>
</body>
</html>
```